Website template and forms
Velvet lantern
Website template and forms  - Financial Services
Creative Brief
Financial Services
http://www.velvet-lantern.co.uk
Velvet Lantern works as an intermediary between clients who are looking into products such as life insurance and the IFA and Brokerage community who can assist them.
We have teamed up with some of the countries largest survey companies and respond directly to customers who have suggested they may be interested in learning more.
General knowledge about life insurance and how it operates is limited within what the industry terms “the insurance gap” and our aim is to ensure our customers understand the products they are interested in and they feel the products are suitable for them.
Whilst we do not provide or offer advice at any time, we spend time talking with customers about their need for cover. We find a lot of our customers have made the decision that they need to have cover in place but have yet to think about how much cover they require and over what time period. This can cause difficulties when calling into brokerages directly or indeed when using comparison sites, where you are asked direct questions and are not always equipped with the answers. This can then be a frustrating process for all involved.
We have essentially two sets of customers, the customers who respond to surveys and whom we then call and assist and also the IFA/Brokerages with whom we place our leads.
We will only transfer a client to a brokerage when they have a good understanding of what they are looking for, often we can outline the areas to think about and arrange to call the client back. This works for everyone concerned as the buyer knows what they are looking for and understands what the product does and doesn’t do and also ensures that the commercial side of our business, which is lead provision maintains its reputation.
We have long term relationships with our clients and companies have chosen us as their sole partner for Life insurance transfers. We work continually on our approach and service so that brokerages receive those customers whom they feel they can benefit; taking daily feedback on every lead we supply to ensure standards are high.
Each brokerage has its own set of criteria and parameters for customers, for example IFA companies who like to advise clients need the customers to have enough time to spare to complete a fact find and have their needs assessed. Brokerages offer a quick and comprehensive service often finding customers much more competitive products than they would otherwise have access to.
Like : Exisiting logo. Dislikes: Flash, moving images, unindexable content
Colorful
Humorous
yellow
what ever works
Arial, Verdana, Trebuchet MS, Times New Roman, Century Gothic, Georgia
left side
please email derek@velvet-lantern.co.uk for the full design brief. We also need some auto email forms creating as part of the project. Please inform me if you cannot do this.

```html
<!DOCTYPE html>
<html lang="en">
<head>
<meta charset="utf-8">
<title>Velvet Lantern – Financial Services</title>
<link rel="stylesheet" href="https://fonts.googleapis.com/css2?family=Arimo:wght@400;700&family=Tinos:wght@400;700&display=swap">
<style>
  :root {
    --white: #ffffff;
    --ink: #2b2b2b;
    --grey-text: #7a7a7a;
    --panel-grey: #efefef;
    --panel-line: #dcdcdc;
    --navy-deep: #0d0f5c;
    --navy: #1d2a9a;
    --navy-light: #3f5fd0;
    --orange: #f7a21b;
    --orange-deep: #e07c06;
    --orange-light: #ffc94a;
    --blue-head: #1a4fa8;
    --footer: #9a9a9a;
  }
  * { box-sizing: border-box; margin: 0; padding: 0; }
  html, body { width: 1200px; height: 901px; overflow: hidden; background: var(--white); }
  body { position: relative; font-family: "Arimo", Arial, sans-serif; color: var(--ink); }

  .site-header { position: absolute; left: 0; top: 0; width: 1200px; height: 122px; background: var(--white); }
  .brand { position: absolute; left: 28px; top: 34px; display: flex; align-items: center; gap: 12px; }
  .brand-dot { width: 38px; height: 38px; border-radius: 50%; background: var(--navy); }
  .brand-name { font-weight: 700; font-size: 26px; color: var(--navy); line-height: 1; white-space: nowrap; }

  .main-nav a { position: absolute; top: 0; height: 80px; padding-top: 30px; font-size: 19px; line-height: 1;
    color: var(--navy); text-decoration: none; white-space: nowrap; text-align: center; }
  .nav-about { left: 689px; width: 124px; background: linear-gradient(var(--orange-light), var(--orange)); }
  .nav-home { left: 838px; width: 180px; }
  .nav-contact { left: 1040px; width: 130px; }

  .search { position: absolute; left: 991px; top: 82px; width: 172px; height: 28px; border: 3px solid var(--orange); border-radius: 6px; background: var(--white); display: flex; align-items: center; }
  .search span { font-size: 11px; color: var(--navy); padding-left: 10px; flex: 1; letter-spacing: .5px; }
  .search svg { margin-right: 3px; }

  .hero { position: absolute; left: 0; top: 122px; width: 1200px; height: 389px; overflow: hidden;
    background: radial-gradient(ellipse at 40% 35%, var(--navy-light) 0%, var(--navy) 45%, var(--navy-deep) 100%); }
  .hero-mascot { position: absolute; left: 10px; top: 10px; width: 240px; height: 370px;
    background: radial-gradient(ellipse 50% 48% at 50% 45%, rgba(90,140,230,.75), rgba(60,90,200,.35) 60%, rgba(30,42,154,0) 100%); }
  .hero-name { position: absolute; left: 180px; top: 128px; font-weight: 700; font-size: 58px; line-height: 1; color: var(--white); white-space: nowrap; }
  .hero-name span { display: block; color: var(--orange-light); font-size: 62px; letter-spacing: 1px; }
  .hero-clipboard { position: absolute; left: 520px; top: 50px; width: 240px; height: 240px; transform: rotate(-10deg);
    background: radial-gradient(ellipse 50% 50% at 50% 50%, rgba(240,236,226,.9), rgba(222,168,80,.6) 65%, rgba(222,168,80,0) 100%); }

  .offer-panel { position: absolute; left: 852px; top: 36px; width: 348px; height: 244px;
    background: linear-gradient(var(--orange-light), var(--orange-deep)); border: 2px solid var(--orange-light); border-right: none; }
  .offer-panel .lead { background: var(--white); color: var(--orange-deep); font-size: 18px; padding: 6px 10px 0; white-space: nowrap; }
  .offer-panel ul { list-style: none; }
  .offer-panel li { font-size: 21px; color: var(--navy-deep); padding: 0 10px; height: 58px; line-height: 58px; border-bottom: 2px solid var(--orange-light); white-space: nowrap; }
  .offer-panel li.first { background: var(--white); height: 34px; line-height: 28px; border-bottom: 3px solid var(--orange-deep); }
  .offer-panel li:last-child { border-bottom: none; }
  .signup { position: absolute; left: 973px; top: 292px; width: 135px; height: 39px; border-radius: 6px;
    background: linear-gradient(var(--orange-light), var(--orange-deep)); color: var(--navy-deep); font-size: 16px; text-align: center; line-height: 39px; white-space: nowrap; }

  .welcome { position: absolute; left: 0; top: 511px; width: 1200px; height: 358px; background: linear-gradient(var(--white), #f7f7f7); }
  .welcome h1 { position: absolute; left: 46px; top: 16px; font-family: "Tinos", "Times New Roman", serif; font-weight: 400; font-size: 42px; color: var(--blue-head); letter-spacing: 1px; white-space: nowrap; }
  .welcome h2 { position: absolute; left: 56px; top: 62px; font-weight: 400; font-size: 28px; color: var(--orange); white-space: nowrap; }
  .social { position: absolute; left: 795px; top: 20px; display: flex; gap: 10px; }
  .social span { width: 50px; height: 50px; border-radius: 50%; background: #c9c9c9; display: block; }
  .social span.mid { background: #3b5aa0; }
  .social span.last { background: #d8dde8; }
  .lamp { position: absolute; left: 960px; top: 20px; width: 230px; height: 90px;
    background: radial-gradient(ellipse 50% 45% at 60% 60%, rgba(247,162,27,.85), rgba(255,201,74,.4) 65%, rgba(255,201,74,0) 100%); }

  .column { position: absolute; top: 109px; width: 292px; height: 232px; background: var(--panel-grey); border: 1px solid var(--panel-line); padding: 12px 14px; }
  .column h3 { font-weight: 400; font-size: 16px; color: var(--orange); margin-bottom: 8px; }
  .column p { font-size: 12.5px; line-height: 1.3; color: var(--grey-text); margin-bottom: 14px; }
  .col-about { left: 44px; }
  .col-comment { left: 360px; }
  .col-news { left: 682px; }
  .more { position: absolute; right: 14px; bottom: 8px; font-size: 11px; color: var(--orange); }
  .field { display: flex; align-items: flex-start; margin-bottom: 10px; font-size: 13px; color: var(--navy); }
  .field label { width: 104px; padding-top: 6px; white-space: nowrap; }
  .field .input { flex: 1; height: 28px; background: var(--white); border: 1px solid #c4c4c4; }
  .field.short label { width: 48px; }
  .field.tall .input { height: 70px; }
  .news-date { color: var(--orange); font-size: 13px; margin-bottom: 2px; }

  .site-footer { position: absolute; left: 0; top: 869px; width: 1200px; height: 32px; background: var(--footer); color: #333; font-family: "Tinos", "Times New Roman", serif; font-size: 13px; text-align: center; line-height: 32px; }
</style>
</head>
<body>
  <header class="site-header">
    <div class="brand"><span class="brand-dot"></span><span class="brand-name">Velvet Lantern</span></div>
    <nav class="main-nav">
      <a class="nav-about" href="#">ABOUT US</a>
      <a class="nav-home" href="#">HOME INSURANCE</a>
      <a class="nav-contact" href="#">CONTACT US</a>
    </nav>
    <div class="search">
      <span>SEARCH</span>
      <svg width="22" height="20" viewBox="0 0 22 20"><rect width="22" height="20" rx="4" fill="#1d2a9a"/><circle cx="10" cy="9" r="4" fill="none" stroke="#fff" stroke-width="2"/><line x1="13" y1="12" x2="17" y2="16" stroke="#fff" stroke-width="2"/></svg>
    </div>
  </header>

  <section class="hero">
    <div class="hero-mascot" role="img" aria-label="Illustration of a friendly lantern spirit mascot"></div>
    <div class="hero-name">Velvet<span>LANTERN</span></div>
    <div class="hero-clipboard" role="img" aria-label="Illustration of a clipboard checklist with a pencil"></div>
    <div class="offer-panel">
      <div class="lead">over 50 live insurance no</div>
      <ul>
        <li class="first">MEDICALES</li>
        <li>LIVE INSURANCE</li>
        <li>BROKEN AREA</li>
      </ul>
    </div>
    <div class="signup">SIGN UP NOW</div>
  </section>

  <main class="welcome">
    <h1>WELCOME TO</h1>
    <h2>Velvet lantern world</h2>
    <div class="social" aria-label="Social links"><span></span><span class="mid"></span><span class="last"></span></div>
    <div class="lamp" role="img" aria-label="Illustration of a golden oil lamp"></div>

    <article class="column col-about">
      <h3>VELVET LANTERN</h3>
      <p>works as an intermediary between clients who are looking into products such as life insurance and the IFA and Brokerage community who can assist them.</p>
      <p>We have teamed up with some of the countries largest survey companies and respond directly to customers who have suggested they may be interested in learning more.</p>
      <span class="more">read more &gt;&gt;</span>
    </article>

    <form class="column col-comment">
      <h3>LIVE A COMMENT</h3>
      <div class="field short"><label>NEME</label><div class="input"></div></div>
      <div class="field"><label>EMAIL ADRESS</label><div class="input"></div></div>
      <div class="field tall"><label>MESSAGE</label><div class="input"></div></div>
    </form>

    <article class="column col-news">
      <h3>NEWS</h3>
      <div class="news-date">4.5.2010</div>
      <p>Aenean interdum<br>Vestibulum ante ipsum primis into faucibus orci luctus ultrices antame posuere.</p>
      <div class="news-date">4.5.2010</div>
      <p>Integer vitae nisl<br>Duis volutpat ligula laoreet orci luctus ultrices.</p>
      <span class="more">read more &gt;&gt;</span>
    </article>
  </main>

  <footer class="site-footer">©Copyright <b>SiteName</b>. All Rights Reserved.</footer>
</body>
</html>
```